Design a business card & stationary for a mortgage company

We are looking for a good looking business card design for our mortgage company that includes our logo. We received a free design as part of our logo project but we don't love it. The company is called "Birchfield Mortgage Company" so we like waves and lighthouses. The logo should be included. We have a version in both vertical and horizontal that we have provided.

Industry/Entity Type

Finance

Contact Information for Business Card

This should include our new logo file

Requirements
Must have
• 3. The details you'd like on the card - name, title, phone, email, website, address, social media handles etc.
1. Dennis Marlow
Vice President
614-390-2751
Fax 877-402-6158
dmarlow@birchfieldmortgage.example
NMLS 47192 - Company NMLS 62304
18 Elm Ave
Marsh Harbor, DE 08512

```html
<!DOCTYPE html>
<html lang="en">
<head>
<meta charset="utf-8">
<title>Birchfield Mortgage Company – Business Card</title>
<link rel="stylesheet" href="https://fonts.googleapis.com/css2?family=Jost:wght@400;500&display=swap">
<style>
  :root {
    --backdrop: #8a8a8a;
    --brand-blue: #125a93;
    --wave-blue: #0094d9;
    --sky-blue: #2d9be0;
    --paper: #ffffff;
    --ink: #4a4a4a;
  }
  * { margin: 0; padding: 0; box-sizing: border-box; }
  html, body {
    width: 1200px; height: 1200px; overflow: hidden;
    background: var(--backdrop);
    font-family: "Jost", sans-serif;
  }
  .card {
    position: absolute; left: 262px; width: 686px; height: 392px;
    border-radius: 22px; overflow: hidden;
  }
  .card--front { top: 165px; background: var(--brand-blue); }
  .card--back { top: 653px; background: var(--brand-blue); }

  .front-wave { position: absolute; inset: 0; width: 100%; height: 100%; }

  .holder { position: absolute; top: 42px; right: 34px; text-align: right; color: var(--paper); }
  .holder__name { font-size: 24px; font-weight: 500; letter-spacing: 0.2px; line-height: 1.1; }
  .holder__title { font-size: 16px; font-weight: 400; margin-top: 1px; }

  .brand { font-weight: 500; color: var(--brand-blue); line-height: 1; display: flex; align-items: center; gap: 12px; }
  .brand__dot { width: 14px; height: 14px; border-radius: 50%; background: var(--brand-blue); flex: none; }
  .brand__name { font-size: 40px; letter-spacing: -0.5px; }
  .brand__sub { display: block; font-size: 12px; letter-spacing: 4.6px; margin-top: 6px; }
  .card--front .brand { position: absolute; left: 37px; top: 160px; }

  .contact { position: absolute; left: 34px; top: 302px; list-style: none; color: var(--ink); font-size: 16px; line-height: 19.5px; }
  .contact li { display: flex; align-items: center; gap: 8px; }
  .contact svg { width: 13px; height: 13px; fill: var(--brand-blue); flex: none; }

  .address { position: absolute; right: 34px; top: 304px; text-align: right; color: var(--ink); font-size: 16px; line-height: 19.5px; font-style: normal; }

  .card--back .brand { position: absolute; left: 136px; top: 150px; color: var(--sky-blue); }
  .card--back .brand__dot { background: var(--sky-blue); width: 18px; height: 18px; }
  .card--back .brand__name { font-size: 54px; }
  .card--back .brand__sub { font-size: 16px; letter-spacing: 6px; margin-top: 8px; }
</style>
</head>
<body>
  <section class="card card--front" aria-label="Business card front">
    <svg class="front-wave" viewBox="0 0 800 457" preserveAspectRatio="none" aria-hidden="true">
      <path d="M0 162 C40 100 90 40 165 40 C260 40 330 80 430 115 C560 160 700 188 800 148 V457 H0 Z" fill="var(--paper)"/>
      <path transform="translate(0 4)" d="M0 162 C40 100 90 40 165 40 C260 40 330 80 430 115 C560 160 700 188 800 148 V457 H0 Z" fill="var(--wave-blue)"/>
      <path transform="translate(0 14)" d="M0 162 C40 100 90 40 165 40 C260 40 330 80 430 115 C560 160 700 188 800 148 V457 H0 Z" fill="var(--paper)"/>
    </svg>

    <div class="holder">
      <p class="holder__name">DENNIS MARLOW</p>
      <p class="holder__title">Vice President</p>
    </div>

    <div class="brand">
      <span class="brand__dot"></span>
      <p class="brand__name">BIRCHFIELD<span class="brand__sub">MORTGAGE COMPANY</span></p>
    </div>

    <ul class="contact">
      <li><svg viewBox="0 0 24 24"><path d="M6.6 10.8a15.1 15.1 0 0 0 6.6 6.6l2.2-2.2c.3-.3.7-.4 1-.2 1.1.4 2.3.6 3.6.6.6 0 1 .4 1 1V20c0 .6-.4 1-1 1A17 17 0 0 1 3 4c0-.6.4-1 1-1h3.5c.6 0 1 .4 1 1 0 1.3.2 2.5.6 3.6.1.3 0 .7-.2 1z"/></svg>614-390-2751</li>
      <li><svg viewBox="0 0 24 24"><path d="M2 5h20v14H2z M2 5l10 8 10-8" fill="none" stroke="var(--brand-blue)" stroke-width="2.5"/></svg>dmarlow@birchfieldmortgage.example</li>
      <li><svg viewBox="0 0 24 24"><circle cx="12" cy="12" r="10"/><path d="M2 12h20M12 2c3 3 3 17 0 20M12 2c-3 3-3 17 0 20" fill="none" stroke="#fff" stroke-width="1.5"/></svg>www.birchfieldmortgage.example</li>
    </ul>

    <address class="address">
      NMLS 47192 · Company<br>
      NMLS 62304, 18 Elm Ave<br>
      Marsh Harbor, DE 08512
    </address>
  </section>

  <section class="card card--back" aria-label="Business card back">
    <div class="brand">
      <span class="brand__dot"></span>
      <p class="brand__name">BIRCHFIELD<span class="brand__sub">MORTGAGE COMPANY</span></p>
    </div>
  </section>
</body>
</html>
```